Law Firm Needs a new Website Design

We need a new website design for our law firm located in Manhattan (Law Offices of Tobias R. Venkland, PLLC).
We have an existing logo that we will to continue using, which can be found in www.VenklandLaw.example.
The Prime Counsel, Top Advocates Logo should also be reflected near the bottom of the Home page.
The website will be 6 pages.

Deliverables:
I want a
1) home page,
2) About Us/Practice Areas page,
3) attorneys,
4) News and Articles page, and
5) Contact and Directions/Privacy Policy page.

The colors of my logo should be in the website.
I also like a touch of black and red.

The website should project "excellence."
We seek to provide the highest quality legal services.
We handle estate planning, wills, trusts, planning for people with disabilities, asset protection and preservation, Medicaid planning, hospital safe discharge, nursing home placement, powers of attorney, health care proxies, living wills, guardianships, probate, estate administration and related litigation.

I would like the colors of my Logo used (including shading where appropriate).
I also want some black on the borders and/or bottom and some red touches throughout the page.

My Logo should appear everywhere that "Law Offices Of Tobias R. Venkland, PLLC" appears.
I want the badges for Prime counsel, Top Advocates, Top Legal Practices, and ZELQ on the Home page.
I do not want too much text on the home page.

We would also like the website to have coding.
The final design should also communicate quality, expertise and stability.
Great start so far by the people who submitted designs.
Thank you.

Industry/Entity Type

Law Firm

Coding

Coded - Design and coding required

Number of Pages Required

5+ page

Colors
3276b5
ec1f27
474747

Requirements
Must have
• Please use my logo each time you mention Law Offices of Tobias R. Venkland, PLLC. Please include the Primecounsel, Top Advocates, Top Legal Practices and Zelq rating Badges on the web home page. I only wish to be contacted by phone. I am not including testimonials and am only using the New York City address.
Nice to have
• Prefer illustrations to photos regarding practice areas
Should not have
• Testimonials, contact me by email, free consultation.

```html
<!DOCTYPE html>
<html lang="en">
<head>
<meta charset="utf-8">
<title>Law Offices of Tobias R. Venkland, PLLC</title>
<link rel="stylesheet" href="https://fonts.googleapis.com/css2?family=Montserrat:wght@400;600;700&family=Open+Sans:wght@400;600;700&display=swap">
<style>
:root{
  --blue:#3276b5;
  --red:#ec1f27;
  --charcoal:#474747;
  --dark:#3c3c3c;
  --white:#ffffff;
  --line:#e4e4e4;
  --text:#333333;
}
*{box-sizing:border-box;margin:0;padding:0}
html,body{width:668px;height:1200px;overflow:hidden;background:var(--white)}
body{position:relative;font-family:"Open Sans",Arial,sans-serif;color:var(--text)}
.abs{position:absolute}

/* hero */
.hero{left:0;top:0;width:668px;height:338px;
  background:linear-gradient(100deg,#2a2a2c 0%,#4a4a4c 30%,#6a6a6a 50%,#3b3b3d 75%,#242426 100%)}
.hero::after{content:"";position:absolute;inset:0;background:rgba(0,0,0,.25)}
.masthead{left:0;top:22px;width:668px;height:63px;background:rgba(235,235,235,.88);z-index:2}
.brand{left:92px;top:19px;display:flex;align-items:center;gap:8px}
.brand-mark{width:22px;height:22px;background:var(--blue)}
.brand-name{font-family:"Montserrat",sans-serif;font-weight:600;font-size:13px;color:var(--charcoal);letter-spacing:.2px}
.masthead-contact{right:53px;top:22px;text-align:right;font-family:"Open Sans",sans-serif;color:var(--blue)}
.masthead-contact .phone{font-size:11px;font-weight:700;letter-spacing:.3px}
.masthead-contact .area{font-size:7.5px;font-weight:700;letter-spacing:.2px}
.hero-title{left:84px;top:155px;width:500px;text-align:center;z-index:2;
  font-family:"Montserrat",sans-serif;font-weight:700;font-size:21.5px;line-height:29.5px;color:var(--white)}
.btn-blue{background:var(--blue);color:var(--white);font-family:"Montserrat",sans-serif;font-weight:600;
  display:flex;align-items:center;justify-content:center;gap:8px}
.hero-btn{left:284px;top:265px;width:102px;height:18px;font-size:8.5px;z-index:2}

/* nav */
.nav{left:0;top:338px;width:668px;height:33px;background:var(--charcoal);display:flex;gap:0;padding-left:100px}
.nav a{font-family:"Open Sans",sans-serif;font-weight:600;font-size:7px;color:var(--white);text-decoration:none;
  height:33px;line-height:33px;margin-right:19px;position:relative;letter-spacing:-.1px}
.nav a.active::after{content:"";position:absolute;left:0;right:0;bottom:3px;height:2px;background:var(--blue)}

/* welcome */
.welcome{left:84px;top:413px;width:500px;text-align:center;font-family:"Montserrat",sans-serif;
  font-weight:600;font-size:16.5px;line-height:22px;color:var(--red)}

/* results */
.results{left:0;top:492px;width:668px;height:119px;
  background:linear-gradient(180deg,#2b2b2b,#4b4b4b 50%,#2e2e2e)}
.result{top:38px;text-align:center;color:var(--white)}
.result .label{font-size:7.5px;font-weight:600}
.result .value{font-family:"Montserrat",sans-serif;font-size:17.5px;font-weight:700;margin-top:6px}
.results-btn{left:462px;top:34px;width:132px;height:50px;background:var(--white);text-align:center;padding-top:8px}
.results-btn span{display:block;font-size:8.5px;font-weight:700;color:var(--charcoal);margin-bottom:4px}

/* practice */
.section-title{left:84px;top:652px;width:500px;text-align:center;font-family:"Montserrat",sans-serif;
  font-weight:600;font-size:16.5px;color:var(--red)}
.rule{left:70px;top:684px;width:527px;height:4px;border-top:2px solid var(--line);border-bottom:1px solid var(--line)}
.card{top:716px;width:121px;border:1px solid var(--line);background:var(--white);text-align:center;padding-top:18px}
.card svg.icon{display:block;margin:0 auto}
.card .name{font-size:7px;font-weight:700;color:var(--charcoal);margin-top:7px;line-height:10px;padding:0 10px;height:20px}
.card .go{position:absolute;left:50%;bottom:-10px;transform:translateX(-50%);width:18px;height:16px;
  border:1px solid var(--line);background:var(--white);display:flex;align-items:center;justify-content:center}
.all-btn{left:271px;top:854px;width:124px;height:20px;font-size:7.5px}

/* footer */
.footer{left:0;top:912px;width:668px;height:179px;background:var(--red);color:var(--white)}
.fcol{top:28px}
.fcol h4{font-family:"Montserrat",sans-serif;font-weight:600;font-size:11.5px;margin-bottom:9px}
.fcol li{list-style:none;font-size:7px;line-height:15.2px}
.contact p{font-size:7.5px;font-weight:600;line-height:9.5px}
.badge{background:rgba(255,255,255,.9)}
.bottom{left:0;top:1091px;width:668px;height:109px;background:var(--charcoal)}
.social{left:293px;top:36px;display:flex;gap:14px}
.social span{width:17px;height:17px;background:var(--blue);border-radius:2px;display:block}
.copyright{left:0;top:67px;width:668px;text-align:center;font-size:10px;color:#9a9a9a}
</style>
</head>
<body>

<div class="abs hero" role="img" aria-label="Photo of attorneys in suits conversing in an office overlooking the city"></div>

<header class="abs masthead">
  <div class="abs brand">
    <span class="brand-mark"></span>
    <span class="brand-name">Law Offices of Tobias R. Venkland, PLLC</span>
  </div>
  <div class="abs masthead-contact">
    <div class="phone">(212).555.0147</div>
    <div class="area">SERVING THE STATE OF NEW YORK</div>
  </div>
</header>

<h1 class="abs hero-title">Our firm was founded in 1993 by Tobias R. Venkland, a member of the National Guild of Estate Counsel (NGEC).</h1>
<a class="abs btn-blue hero-btn">CONTACT US
  <svg width="10" height="9" viewBox="0 0 10 9"><rect x="0.5" y="1" width="4" height="7" fill="none" stroke="#fff" stroke-width="1"/><path d="M4 3h3V1l3 3.5L7 8V6H4z" fill="#fff"/></svg>
</a>

<nav class="abs nav">
  <a class="active">HOME</a><a>ABOUT US</a><a>PRACTICE AREAS</a><a>ATTORNEYS</a><a>NEWS &amp; ARTICLES</a><a>PRIVACY &amp; POLICY</a><a>CONTACT &amp; DIRECTION</a>
</nav>

<h2 class="abs welcome">WELCOME TO Law Offices of Tobias R. Venkland, PLLC</h2>

<section class="abs results" role="img" aria-label="Aerial view of Manhattan skyscrapers behind case result figures">
  <div class="abs result" style="left:105px;width:92px"><div class="label">Residential</div><div class="value">$ 340,000</div></div>
  <div class="abs result" style="left:218px;width:110px"><div class="label">Commercial</div><div class="value">$ 1,880,350</div></div>
  <div class="abs result" style="left:348px;width:94px"><div class="label">Business</div><div class="value">$ 648,000</div></div>
  <div class="abs results-btn"><span>See All Case Results</span>
    <svg width="15" height="13" viewBox="0 0 10 9"><rect x="0.5" y="1" width="4" height="7" fill="none" stroke="#474747" stroke-width="1"/><path d="M4 3h3V1l3 3.5L7 8V6H4z" fill="#474747"/></svg>
  </div>
</section>

<h2 class="abs section-title">PRACTICE AREAS</h2>
<div class="abs rule"></div>

<div class="abs card" style="left:70px;height:86px">
  <svg class="icon" width="26" height="22" viewBox="0 0 26 22"><path d="M13 1L1 11h3v10h7v-6h4v6h7V11h3z" fill="#474747"/></svg>
  <div class="name">ESTATE PLANNING</div>
  <div class="go"><svg width="8" height="7" viewBox="0 0 10 9"><rect x="0.5" y="1" width="4" height="7" fill="none" stroke="#474747"/><path d="M4 3h3V1l3 3.5L7 8V6H4z" fill="#474747"/></svg></div>
</div>
<div class="abs card" style="left:205px;height:96px">
  <svg class="icon" width="22" height="26" viewBox="0 0 22 26"><rect x="2" y="1" width="18" height="24" fill="none" stroke="#474747" stroke-width="2"/><g fill="#474747"><rect x="5" y="4" width="3" height="3"/><rect x="9.5" y="4" width="3" height="3"/><rect x="14" y="4" width="3" height="3"/><rect x="5" y="9" width="3" height="3"/><rect x="9.5" y="9" width="3" height="3"/><rect x="14" y="9" width="3" height="3"/><rect x="5" y="14" width="3" height="3"/><rect x="9.5" y="14" width="3" height="3"/><rect x="14" y="14" width="3" height="3"/><rect x="9" y="19" width="4" height="6"/></g></svg>
  <div class="name">PROBATE AN ESTATE ADMINISTRATION</div>
  <div class="go"><svg width="8" height="7" viewBox="0 0 10 9"><rect x="0.5" y="1" width="4" height="7" fill="none" stroke="#474747"/><path d="M4 3h3V1l3 3.5L7 8V6H4z" fill="#474747"/></svg></div>
</div>
<div class="abs card" style="left:340px;height:96px">
  <svg class="icon" width="26" height="26" viewBox="0 0 26 26"><g fill="#474747" transform="rotate(45 13 13)"><rect x="5" y="3" width="16" height="8" rx="1"/><rect x="11" y="11" width="4" height="13"/></g></svg>
  <div class="name">SUPPLIMENTAL NEEDS TRUST</div>
  <div class="go"><svg width="8" height="7" viewBox="0 0 10 9"><rect x="0.5" y="1" width="4" height="7" fill="none" stroke="#474747"/><path d="M4 3h3V1l3 3.5L7 8V6H4z" fill="#474747"/></svg></div>
</div>
<div class="abs card" style="left:476px;height:86px">
  <svg class="icon" width="26" height="26" viewBox="0 0 26 26"><circle cx="11" cy="3" r="2.5" fill="#474747"/><path d="M11 7v8h7l3 7" fill="none" stroke="#474747" stroke-width="2.2"/><path d="M8 11a6.5 6.5 0 1 0 9 8" fill="none" stroke="#474747" stroke-width="2"/></svg>
  <div class="name">GUARDIANSHIPS</div>
  <div class="go"><svg width="8" height="7" viewBox="0 0 10 9"><rect x="0.5" y="1" width="4" height="7" fill="none" stroke="#474747"/><path d="M4 3h3V1l3 3.5L7 8V6H4z" fill="#474747"/></svg></div>
</div>

<a class="abs btn-blue all-btn">ALL PRACTICE AREAS</a>

<footer class="abs footer">
  <div class="abs fcol" style="left:96px">
    <h4>MENU</h4>
    <ul><li>Home</li><li>About</li><li>Practice Areas</li><li>Attorneys</li><li>Privacy</li><li>Terms &amp; Conditions</li></ul>
  </div>
  <div class="abs fcol" style="left:218px">
    <h4>LAWYERS</h4>
    <ul><li>Dalen Orvick</li><li>Hollis Brandt</li><li>Teodor Calvi</li><li>Marla Quinby</li><li>Wren Ashdown</li><li>Oskar Lindqvale</li></ul>
  </div>
  <div class="abs fcol contact" style="left:340px">
    <h4>CONTACT INFO</h4>
    <p>Manhattan Office:</p>
    <p>218 Harlow Street, Suite 604<br>New York, New York 10019.</p>
    <p style="margin-top:10px">Phone: (212).555.0147</p>
    <p>Fax: (212).555.0183</p>
  </div>
  <div class="abs badge" style="left:530px;top:30px;width:74px;height:12px" role="img" aria-label="Top Advocates badge"></div>
  <div class="abs badge" style="left:544px;top:50px;width:46px;height:58px" role="img" aria-label="Top Legal Practices badge"></div>
  <div class="abs badge" style="left:528px;top:138px;width:78px;height:12px" role="img" aria-label="Prime Counsel badge"></div>
</footer>

<div class="abs bottom">
  <div class="abs social" aria-label="Social links"><span></span><span></span><span></span></div>
  <div class="abs copyright">@copy All rights reserved</div>
</div>

</body>
</html>
```